Adapt logo for box truck wrap for my restoration company

I need a wrap for our company Brightway Restoration. We specialize in water damage restoration. I’ve attached our logo, business card, and page header. Things I would like to include are- 24 hour emergency service, our phone number (555)014-7392 and that we do water, fire and mold work. It’s a 2004 Kardella Vonter which I’ve attached pictures of. I will get the cab wrapped as well.

Industry/Entity Type

Construction- specifically Restoration

Font styles to use
Sans Serif

Colors

Designer to choose colors to be used in the design.

Requirements
Must have
• Water• Fire• Mold, phone number (555)014-7392
Nice to have
• Clean, professional look with the logo

```html
<!DOCTYPE html>
<html lang="en">
<head>
<meta charset="utf-8">
<title>Brightway Restoration – Box Truck Wrap</title>
<link href="https://fonts.googleapis.com/css2?family=Bebas+Neue&display=swap" rel="stylesheet">
<style>
  :root {
    --wrap-blue: #1284dd;
    --wrap-blue-light: #1c93e6;
    --band-blue: #1180dc;
    --panel-white: #dfe9f3;
    --band-grey: #7a7a7a;
    --logo-grey: #737373;
    --ink: #0a0a0a;
    --text-light: #dfe7ef;
    --page: #ffffff;
  }
  html, body {
    margin: 0;
    padding: 0;
    width: 1094px;
    height: 1200px;
    overflow: hidden;
    background: var(--page);
  }
  .wrap-panel {
    position: absolute;
    left: 47px;
    width: 1000px;
    height: 456px;
    display: block;
  }
  .wrap-panel--driver { top: 110px; }
  .wrap-panel--passenger { top: 640px; }

  .wrap-panel text { font-family: "Bebas Neue", "Oswald", sans-serif; }
  .fill-blue { fill: url(#blueGradient); }
  .fill-band-blue { fill: var(--band-blue); }
  .fill-white { fill: var(--panel-white); }
  .fill-grey { fill: var(--band-grey); }

  .company-name { fill: var(--ink); font-size: 104px; }
  .brand-mark { fill: var(--logo-grey); font-size: 66px; }
  .service-pill { fill: var(--band-grey); }
  .service-label { fill: var(--text-light); font-size: 34px; }
  .phone-number { fill: var(--text-light); font-size: 74px; }
  .services-list { fill: var(--text-light); font-size: 58px; letter-spacing: 1px; }
  .tagline { fill: var(--ink); font-size: 19px; }
  .web-address { fill: var(--text-light); font-size: 19px; }
</style>
</head>
<body>

<!-- Driver side: brand area left, message right -->
<svg class="wrap-panel wrap-panel--driver" viewBox="0 0 1000 456" aria-label="Driver side box wrap">
  <defs>
    <linearGradient id="blueGradient" x1="0" y1="0" x2="1" y2="1">
      <stop offset="0" stop-color="#0f7fd9"/>
      <stop offset="0.5" stop-color="#1a90e4"/>
      <stop offset="1" stop-color="#137fd8"/>
    </linearGradient>
    <clipPath id="panelClip"><rect width="1000" height="456"/></clipPath>
  </defs>
  <g clip-path="url(#panelClip)">
    <rect class="fill-blue" width="1000" height="456"/>
    <rect class="fill-grey" y="387" width="1000" height="69"/>
    <rect class="fill-white" width="224" height="456"/>
    <circle class="fill-white" cx="224" cy="228" r="250"/>
    <polygon class="fill-band-blue" points="0,387 398,387 360,456 0,456"/>
  </g>

  <text class="brand-mark" x="224" y="218" text-anchor="middle">Brightway</text>
  <text class="brand-mark" x="224" y="282" text-anchor="middle">Restoration</text>

  <text class="tagline" x="30" y="414">We specialize in water damage restoration</text>
  <text class="web-address" x="30" y="442">BRIGHTWAYRESTORATIONPRO.COM</text>

  <text class="company-name" x="738" y="118" text-anchor="middle">BRIGHTWAY</text>
  <text class="company-name" x="738" y="214" text-anchor="middle">RESTORATION</text>
  <rect class="service-pill" x="595" y="237" width="286" height="52" rx="26"/>
  <text class="service-label" x="738" y="276" text-anchor="middle">24 HOUR SERVICE</text>
  <text class="phone-number" x="738" y="370" text-anchor="middle">(555)014-7392</text>
  <text class="services-list" x="738" y="442" text-anchor="middle">WATER • FIRE • MOLD</text>
</svg>

<!-- Passenger side: message left, brand area right -->
<svg class="wrap-panel wrap-panel--passenger" viewBox="0 0 1000 456" aria-label="Passenger side box wrap">
  <defs>
    <clipPath id="panelClip2"><rect width="1000" height="456"/></clipPath>
  </defs>
  <g clip-path="url(#panelClip2)">
    <g transform="translate(1000,0) scale(-1,1)">
      <rect class="fill-blue" width="1000" height="456"/>
      <rect class="fill-grey" y="387" width="1000" height="69"/>
      <rect class="fill-white" width="224" height="456"/>
      <circle class="fill-white" cx="224" cy="228" r="250"/>
      <polygon class="fill-band-blue" points="0,387 398,387 360,456 0,456"/>
    </g>
  </g>

  <text class="brand-mark" x="776" y="218" text-anchor="middle">Brightway</text>
  <text class="brand-mark" x="776" y="282" text-anchor="middle">Restoration</text>

  <text class="tagline" x="970" y="414" text-anchor="end">We specialize in water damage restoration</text>
  <text class="web-address" x="970" y="442" text-anchor="end">BRIGHTWAYRESTORATIONPRO.COM</text>

  <text class="company-name" x="262" y="118" text-anchor="middle">BRIGHTWAY</text>
  <text class="company-name" x="262" y="214" text-anchor="middle">RESTORATION</text>
  <rect class="service-pill" x="119" y="237" width="286" height="52" rx="26"/>
  <text class="service-label" x="262" y="276" text-anchor="middle">24 HOUR SERVICE</text>
  <text class="phone-number" x="262" y="370" text-anchor="middle">(555)014-7392</text>
  <text class="services-list" x="262" y="442" text-anchor="middle">WATER • FIRE • MOLD</text>
</svg>

</body>
</html>
```